Top of the line business card design needed for real estate brokerage

We currently have a business card with our logo but would like to have a revised version. We would love for you to implement your own design that will catch anyone's attention. The theme colors should be black, royal blue, gray/silver, and white.The contact information should be the same as the info on our current business card (picture attached). In the design that we pick, we will need to be able to edit the text so that we can customize the text content for each of our agents. Same goes for the professional picture. There should be an area on the card that each agent can have their professional portrait attached. Please include a version without the picture option as well for agents that do not wish to have a professional picture attached.
Business

```html
<!DOCTYPE html>
<html lang="en">
<head>
<meta charset="utf-8">
<title>Clear Harbor Realty – Business Card</title>
<link href="https://fonts.googleapis.com/css2?family=Open+Sans:wght@400;600;700&display=swap" rel="stylesheet">
<style>
  :root {
    --royal-blue: #0b4fa3;
    --ink-blue: #1b3f8f;
    --silver: #b9bcc2;
    --paper: #ffffff;
    --backdrop: #111111;
  }
  * { margin: 0; padding: 0; box-sizing: border-box; }
  html, body { width: 1200px; height: 915px; overflow: hidden; background: var(--backdrop); }
  body { font-family: "Open Sans", Arial, sans-serif; }
  .stage {
    position: relative; width: 1200px; height: 915px;
    display: flex; align-items: center; justify-content: center; gap: 40px;
  }
  .card {
    position: relative; width: 540px; height: 320px;
    background: var(--paper); overflow: hidden;
  }
  .card-shape { position: absolute; inset: 0; width: 100%; height: 100%; }
  .brand-name {
    position: absolute; color: var(--paper);
    font-weight: 700; font-size: 26px; line-height: 1.05;
    display: flex; align-items: center; gap: 10px;
  }
  .brand-name .brand-square { width: 14px; height: 14px; background: var(--paper); flex: none; }
  .front .brand-name { left: 56px; top: 118px; }
  .back .brand-name { right: 34px; top: 222px; font-size: 22px; }

  .services {
    position: absolute; left: 78px; top: 226px;
    display: grid; grid-template-columns: 190px 34px auto; row-gap: 12px;
    color: var(--ink-blue); font-weight: 700; font-size: 15px;
  }
  .services .divider { width: 1px; height: 20px; background: var(--ink-blue); justify-self: center; }

  .agent { position: absolute; left: 55px; top: 56px; color: var(--ink-blue); }
  .agent-name { font-weight: 700; font-size: 21px; text-transform: uppercase; line-height: 1.1; }
  .agent-title { font-size: 15px; padding-left: 18px; }

  .contacts { position: absolute; left: 46px; top: 133px; list-style: none; color: var(--ink-blue); font-size: 14.5px; }
  .contacts li { display: flex; align-items: flex-start; gap: 14px; margin-bottom: 12px; line-height: 1.3; }
  .contacts svg { width: 16px; height: 16px; flex: none; margin-top: 2px; fill: var(--ink-blue); }
</style>
</head>
<body>
<main class="stage">

  <section class="card front" aria-label="Card front">
    <svg class="card-shape" viewBox="0 0 540 320" preserveAspectRatio="none" aria-hidden="true">
      <path d="M0,0 H525 C500,130 320,218 0,222 Z" fill="var(--silver)"/>
      <path d="M0,0 H500 C470,112 300,200 0,206 Z" fill="var(--royal-blue)"/>
    </svg>
    <div class="brand-name"><span class="brand-square"></span><span>Clear Harbor<br>Realty</span></div>
    <div class="services">
      <span>Residental Real Estate</span><span class="divider"></span><span>Commercial Real Estate</span>
      <span>Property Management</span><span class="divider"></span><span>Investments</span>
    </div>
  </section>

  <section class="card back" aria-label="Card back">
    <svg class="card-shape" viewBox="0 0 540 320" preserveAspectRatio="none" aria-hidden="true">
      <path d="M360,0 C396,120 348,268 158,320 H540 V0 Z" fill="var(--silver)"/>
      <path d="M372,0 C406,120 360,270 172,320 H540 V0 Z" fill="var(--royal-blue)"/>
    </svg>
    <div class="agent">
      <p class="agent-name">Mr. Calder Wynn</p>
      <p class="agent-title">Managing Director</p>
    </div>
    <ul class="contacts">
      <li><svg viewBox="0 0 24 24"><path d="M6.6 10.8a15.2 15.2 0 0 0 6.6 6.6l2.2-2.2c.3-.3.7-.4 1-.2 1.1.4 2.3.6 3.6.6.6 0 1 .4 1 1V20c0 .6-.4 1-1 1A17 17 0 0 1 3 4c0-.6.4-1 1-1h3.5c.6 0 1 .4 1 1 0 1.3.2 2.5.6 3.6.1.3 0 .7-.2 1z"/></svg><span>555-210-4837</span></li>
      <li><svg viewBox="0 0 24 24"><path d="M2 5h20v14H2z M2 5l10 8 10-8" fill="none" stroke="var(--ink-blue)" stroke-width="0"/><path d="M2 6l10 7 10-7V5H2z M2 8v11h20V8l-10 7z"/></svg><span>calder@clearharbor.com</span></li>
      <li><svg viewBox="0 0 24 24"><path d="M12 2a10 10 0 1 0 0 20 10 10 0 0 0 0-20zm6.9 6h-3a15 15 0 0 0-1.3-3.9A8 8 0 0 1 18.9 8zM12 4c.8 1.2 1.5 2.5 1.9 4h-3.8c.4-1.5 1.1-2.8 1.9-4zM4.3 14a8 8 0 0 1 0-4h3.4a16 16 0 0 0 0 4zm.8 2h3a15 15 0 0 0 1.3 3.9A8 8 0 0 1 5.1 16zm3-8h-3a8 8 0 0 1 4.3-3.9C8.8 5.3 8.4 6.6 8.1 8zM12 20c-.8-1.2-1.5-2.5-1.9-4h3.8c-.4 1.5-1.1 2.8-1.9 4zm2.3-6H9.7a14 14 0 0 1 0-4h4.6a14 14 0 0 1 0 4zm.3 5.9c.6-1.2 1-2.5 1.3-3.9h3a8 8 0 0 1-4.3 3.9zm1.7-5.9a16 16 0 0 0 0-4h3.4a8 8 0 0 1 0 4z"/></svg><span>www.clearharborrealty.com</span></li>
      <li><svg viewBox="0 0 24 24"><path d="M12 3l10 9h-3v8h-5v-6h-4v6H5v-8H2z"/></svg><span>2200 Harbor View Dr, Suite 310<br>Coral Bend, FL 33990</span></li>
    </ul>
    <div class="brand-name"><span class="brand-square"></span><span>Clear Harbor<br>Realty</span></div>
  </section>

</main>
</body>
</html>
```